Willowmere Pet Farewells - business cards & brand stationary

We already have a logo and the colors and a website. Need a business card designed that will be able to customized to multiple veterinarians who will be partnering with us. The feel needs to be compassionate, comforting with our tagline 'A Gift of Love at Home'. It will be 2 sides.
On the back our platform/partner vets will be customizing each business card with their own service areas, phone numbers, name and title. On the front, i would like to see experimentation with use of our photos, the logo, tagline and a description 'Peaceful and Compassionate At-Home Pet Euthanasia'

```html
<!DOCTYPE html>
<html lang="en">
<head>
<meta charset="utf-8">
<title>Willowmere Pet Farewells – Business Card</title>
<link href="https://fonts.googleapis.com/css2?family=Poppins:ital,wght@0,400;0,500;0,600;1,400&family=Mansalva&display=swap" rel="stylesheet">
<style>
  :root {
    --page-bg: #dcdcdc;
    --brand-blue: #6f8fb6;
    --brand-blue-soft: #7597bf;
    --brand-blue-text: #6e8fbb;
    --brand-pink: #c07fa6;
    --paper-white: #ffffff;
    --photo-light: #d4d4d4;
    --photo-dark: #8a8a8a;
    --back-top: #e6e6ee;
    --back-bottom: #efe4ec;
  }
  html, body {
    margin: 0;
    padding: 0;
    width: 1200px;
    height: 960px;
    overflow: hidden;
    background: var(--page-bg);
  }
  .canvas {
    position: relative;
    width: 1200px;
    height: 960px;
  }
  .card {
    position: absolute;
    top: 126px;
    width: 402px;
    height: 701px;
    border-radius: 20px;
    overflow: hidden;
  }
  .card--front { left: 168px; }
  .card--back { left: 644px; }
  .card svg { display: block; }
  .brand-name {
    font-family: "Poppins", sans-serif;
    font-weight: 600;
    fill: var(--brand-blue-text);
  }
  .tagline {
    font-family: "Poppins", sans-serif;
    font-style: italic;
    font-size: 11px;
    fill: var(--brand-blue-text);
  }
  .service-line {
    font-family: "Mansalva", cursive;
    font-size: 25px;
    letter-spacing: 3px;
    fill: var(--paper-white);
  }
  .holder-name {
    font-family: "Poppins", sans-serif;
    font-weight: 600;
    font-size: 22px;
    fill: var(--paper-white);
  }
  .holder-title {
    font-family: "Poppins", sans-serif;
    font-size: 16px;
    fill: var(--paper-white);
  }
  .contact-text {
    font-family: "Poppins", sans-serif;
    font-weight: 500;
    fill: var(--brand-blue-text);
  }
</style>
</head>
<body>
<main class="canvas">

  <!-- Front side -->
  <section class="card card--front">
    <svg width="402" height="701" viewBox="0 0 402 701">
      <defs>
        <linearGradient id="photo-tone" x1="0" y1="0" x2="1" y2="1">
          <stop offset="0" stop-color="var(--photo-light)"/>
          <stop offset="1" stop-color="var(--photo-dark)"/>
        </linearGradient>
        <linearGradient id="feature-photo-tone" x1="0" y1="0" x2="1" y2="1">
          <stop offset="0" stop-color="#d9b7a8"/>
          <stop offset="0.5" stop-color="#c9c6c2"/>
          <stop offset="1" stop-color="#9c938c"/>
        </linearGradient>
        <filter id="paper" x="0" y="0">
          <feTurbulence type="fractalNoise" baseFrequency="0.9" numOctaves="1" result="n"/>
        </filter>
      </defs>

      <rect class="front-top-band" x="0" y="0" width="402" height="418" fill="var(--brand-blue)"/>
      <rect class="front-logo-band" x="0" y="418" width="402" height="168" fill="var(--paper-white)"/>
      <rect class="front-bottom-band" x="0" y="586" width="402" height="115" fill="var(--brand-blue-soft)"/>

      <!-- Paw print photo frames -->
      <g class="paw-photos">
        <ellipse cx="72" cy="166" rx="40" ry="42" fill="none" stroke="var(--paper-white)" stroke-width="3"/>
        <ellipse cx="72" cy="166" rx="35" ry="37" fill="url(#photo-tone)" role="img" aria-label="Black and white photo of a small white dog being held"/>

        <ellipse cx="150" cy="118" rx="38" ry="48" transform="rotate(-6 150 118)" fill="none" stroke="var(--paper-white)" stroke-width="3"/>
        <ellipse cx="150" cy="118" rx="33" ry="43" transform="rotate(-6 150 118)" fill="url(#photo-tone)" role="img" aria-label="Black and white photo of a dark dog looking up"/>

        <ellipse cx="250" cy="118" rx="38" ry="48" transform="rotate(8 250 118)" fill="none" stroke="var(--paper-white)" stroke-width="3"/>
        <ellipse cx="250" cy="118" rx="33" ry="43" transform="rotate(8 250 118)" fill="url(#photo-tone)" role="img" aria-label="Black and white photo of a cat resting against its owner"/>

        <ellipse cx="324" cy="170" rx="40" ry="41" fill="none" stroke="var(--paper-white)" stroke-width="3"/>
        <ellipse cx="324" cy="170" rx="35" ry="36" fill="url(#photo-tone)" role="img" aria-label="Black and white photo of a small dog wearing a hat"/>

        <g transform="translate(77.5 176) scale(2.33 2.0)">
          <path d="M50,22 C40,2 0,2 2,32 C4,58 35,78 50,98 C65,78 96,58 98,32 C100,2 60,2 50,22 Z"
                fill="none" stroke="var(--paper-white)" stroke-width="1.4"/>
          <g transform="translate(50 55) scale(0.95) translate(-50 -55)">
            <path d="M50,22 C40,2 0,2 2,32 C4,58 35,78 50,98 C65,78 96,58 98,32 C100,2 60,2 50,22 Z"
                  fill="url(#feature-photo-tone)" role="img" aria-label="Photo of a blue-eyed tabby cat held close by its owner"/>
          </g>
        </g>
      </g>

      <!-- Brand name -->
      <circle cx="201" cy="498" r="9" fill="var(--brand-blue-text)"/>
      <text class="brand-name" x="201" y="544" text-anchor="middle" font-size="22">Willowmere Pet Farewells</text>
      <text class="tagline" x="201" y="567" text-anchor="middle">A gift of love at home.</text>

      <!-- Service description -->
      <text class="service-line" x="201" y="640" text-anchor="middle">Peaceful and Compassionate</text>
      <text class="service-line" x="201" y="670" text-anchor="middle">At-Home Pet Euthanasia</text>
    </svg>
  </section>

  <!-- Back side -->
  <section class="card card--back">
    <svg width="402" height="701" viewBox="0 0 402 701">
      <defs>
        <linearGradient id="back-paper" x1="1" y1="0" x2="0" y2="1">
          <stop offset="0" stop-color="var(--back-top)"/>
          <stop offset="1" stop-color="var(--back-bottom)"/>
        </linearGradient>
      </defs>
      <rect class="back-background" x="0" y="0" width="402" height="701" fill="url(#back-paper)"/>

      <!-- Name heart -->
      <g class="name-heart">
        <g transform="translate(66 68) scale(2.44 2.02)">
          <path d="M50,22 C40,2 0,2 2,32 C4,58 35,78 50,98 C65,78 96,58 98,32 C100,2 60,2 50,22 Z"
                fill="none" stroke="var(--brand-blue)" stroke-width="1.3"/>
        </g>
        <g transform="translate(71 64) scale(2.42 2.0)">
          <path d="M50,22 C40,2 0,2 2,32 C4,58 35,78 50,98 C65,78 96,58 98,32 C100,2 60,2 50,22 Z"
                fill="var(--brand-pink)"/>
        </g>
        <text class="holder-name" x="196" y="173" text-anchor="middle">John Doe</text>
        <text class="holder-title" x="196" y="192" text-anchor="middle">Manager</text>
      </g>

      <!-- Brand name -->
      <circle cx="196" cy="368" r="9" fill="var(--brand-blue-text)"/>
      <text class="brand-name" x="196" y="406" text-anchor="middle" font-size="22">Willowmere Pet Farewells</text>

      <!-- Location -->
      <g class="icon-pin" fill="var(--brand-pink)">
        <path d="M201,470 C193,470 188,476 188,483 C188,491 201,503 201,503 C201,503 214,491 214,483 C214,476 209,470 201,470 Z"/>
        <circle cx="201" cy="482" r="4.5" fill="var(--back-top)"/>
        <rect x="191" y="507" width="20" height="2" rx="1"/>
      </g>
      <text class="contact-text" x="201" y="537" text-anchor="middle" font-size="19">Service area,</text>
      <text class="contact-text" x="201" y="560" text-anchor="middle" font-size="19">State, Postal Code</text>

      <!-- Phone & web icons -->
      <g class="icon-phone">
        <circle cx="188" cy="612" r="9" fill="var(--brand-pink)"/>
        <path d="M184,607 l2,-1 2,3 -1.5,1.2 c0.8,1.8 2,3 3.8,3.8 l1.2,-1.5 3,2 -1,2 c-5,0 -9.5,-4.5 -9.5,-9.5 z" fill="var(--paper-white)"/>
      </g>
      <g class="icon-web" fill="none" stroke="var(--paper-white)" stroke-width="1.1">
        <circle cx="212" cy="612" r="9" fill="var(--brand-pink)" stroke="none"/>
        <circle cx="212" cy="612" r="5.5"/>
        <ellipse cx="212" cy="612" rx="2.4" ry="5.5"/>
        <line x1="206.5" y1="612" x2="217.5" y2="612"/>
      </g>
      <text class="contact-text" x="201" y="646" text-anchor="middle" font-size="17">+12 345 6789</text>
      <text class="contact-text" x="201" y="666" text-anchor="middle" font-size="17">www.willowmerefarewells.com</text>
    </svg>
  </section>

</main>
</body>
</html>
```